Restaurant Poster Design Project for A-Frame

I am after a poster, which will go on an outdoor A-Frame (A1 size - this size is to be confirmed) outlining our drink/happy hour/specials for our Mexican Restaurant and Bar.

Specific details are:

$4 Beer, Wine and Spirits
$5 Margaritas
everynight 5:30pm-7:30pm

I will supply logo, which needs to be incorporated (really small) into the poster, along with our address: 42 Lowden Road, Windsor - (Im not too sure if we should include our phone number or not ?? Please advise what you feel will look good etc

Happy for you to add a phrase or wording etc, as long as the specific details are included, above.

We also have an enclosed beer garden in the rear of the restaurant - Do you believe I should mention this?

I am really open to eye catching designs and ALL suggestions welcome please!
Updates

Please find attached of samples that I am sort of after: (please let me know if they cant be opened).

http://www.flyerquill.example/blog/wp-content/uploads/2012/06/happyHourPoster-e1340372894746.gif

http://marekvu.files.samplepress.example/2012/10/profolio_0012.jpg?w=1169

http://3.img.noteleaf.example/-NfNjpdG5w/T5pohPd0AhI/AAAAAAAADRs/CA7DPeI_PyU/s640/vintage_poster.jpg

http://www.orchidvane.example/files/imagecache/Event/news/teaser/Lounge_Happy_Hour_Poster_-_Mar_2011_bilingual.jpg

http://www.tkrumps.example/dallas/images/happyhour_poster.jpg

http://cdn2-b.newsgrove.example/sites/default/files/styles/large_lightbox/hash/9a/d1/9ad11350ba178511886fddcff7aaac8d.jpg?itok=wDl2vlfJ

http://www.platterpicks.example/imageservice/images/13/1313171414293_244/img_large_watermarked.jpg

Target Market(s)

18 YEARS OLD AND OVER

Industry/Entity Type

Restaurant

Requirements
Must have
• Address
Phone Number
Logo
Clear easy to read font, to be seen via cars + ppl walking down street
If images are included, to be clear and visable
Nice to have
• Images are possible
To mention a beer garden
Should not have
• Traditional Mexican Colourful 80's Theme

```html
<!DOCTYPE html>
<html lang="en">
<head>
<meta charset="utf-8">
<title>Happy Hour – Casa Marlo</title>
<link href="https://fonts.googleapis.com/css2?family=Anton&family=Bebas+Neue&display=swap" rel="stylesheet">
<style>
  :root {
    --ink: #000000;
    --paper: #ffffff;
    --chili: #c8211c;
    --ember: #e0622a;
    --lime: #8fbf3a;
    --agave: #2f7d3b;
    --salt: #efe6cf;
    --sun: #e9c23c;
    --brand: #e7b43a;
  }
  * { margin: 0; padding: 0; box-sizing: border-box; }
  html, body { width: 849px; height: 1200px; overflow: hidden; background: var(--ink); }
  .poster {
    position: relative;
    width: 849px;
    height: 1200px;
    background: var(--ink);
    color: var(--paper);
    font-family: "Bebas Neue", "Oswald", sans-serif;
    overflow: hidden;
  }
  .photo-drinks {
    position: absolute; left: 0; top: 0; width: 849px; height: 345px;
    background:
      linear-gradient(180deg, rgba(0,0,0,0) 60%, rgba(0,0,0,0.35) 100%),
      linear-gradient(90deg, #5a0d0b 0%, var(--chili) 18%, #e88a6a 30%, var(--salt) 45%, var(--sun) 55%, #b8d07a 68%, var(--lime) 80%, var(--agave) 100%);
  }
  .photo-bar {
    position: absolute; left: 0; top: 345px; width: 849px; height: 310px;
    background:
      linear-gradient(180deg, rgba(0,0,0,0.15) 0%, rgba(0,0,0,0.55) 100%),
      linear-gradient(90deg, #7a1510 0%, var(--chili) 20%, var(--ember) 38%, var(--sun) 55%, #9fae3a 72%, var(--agave) 100%);
  }
  .headline {
    position: absolute; left: 0; top: 0; width: 849px; height: 655px;
  }
  .headline text {
    font-family: "Anton", "Impact", sans-serif;
    fill: var(--ink);
  }
  .offer {
    position: absolute; left: 0; top: 664px; width: 849px;
    text-align: center; text-transform: uppercase; line-height: 1;
    white-space: nowrap;
  }
  .offer .intro { font-size: 57px; letter-spacing: 1px; display: block; }
  .offer .intro + .intro { margin-top: 6px; }
  .offer .deal { font-size: 64px; letter-spacing: 1px; display: block; margin-top: 4px; }
  .offer .deal + .deal { margin-top: 0; }
  .offer .hours { font-size: 40px; letter-spacing: 1px; display: block; margin-top: 0; }
  .brand {
    position: absolute; left: 22px; top: 996px; width: 200px;
    display: flex; align-items: center; gap: 10px;
  }
  .brand .dot { width: 26px; height: 26px; border-radius: 50%; background: var(--brand); flex: none; }
  .brand .name { font-size: 50px; line-height: 0.95; color: var(--brand); letter-spacing: 1px; }
  .address {
    position: absolute; left: 388px; top: 992px; width: 135px;
    font-size: 24px; line-height: 1.05; text-transform: uppercase; letter-spacing: 0.3px;
    font-style: normal; white-space: nowrap;
  }
  .contact {
    position: absolute; left: 0; top: 0; width: 849px; height: 1200px;
    pointer-events: none;
  }
  .contact .square { fill: var(--paper); }
  .contact text {
    font-family: "Bebas Neue", "Oswald", sans-serif;
    fill: var(--paper);
    text-transform: uppercase;
  }
</style>
</head>
<body>
<main class="poster">
  <div class="photo-drinks" role="img" aria-label="Photo of three salt-rimmed margarita glasses in red, yellow and green with lime wedges"></div>
  <div class="photo-bar" role="img" aria-label="Warm-toned photo of the restaurant bar interior in red, yellow and green"></div>

  <svg class="headline" width="849" height="655" viewBox="0 0 849 655" aria-label="Happy Hour">
    <text x="42" y="318" font-size="360" textLength="764" lengthAdjust="spacingAndGlyphs">HAPPY</text>
    <text x="42" y="640" font-size="318" textLength="764" lengthAdjust="spacingAndGlyphs">HOUR</text>
  </svg>

  <section class="offer">
    <span class="intro">Enjoy a good time in our beer garden</span>
    <span class="intro">with this special</span>
    <span class="deal">Beer, wine and spirits – only $4</span>
    <span class="deal">Margaritas – only $5</span>
    <span class="hours">Everynight 5:30pm–7:30pm</span>
  </section>

  <div class="brand">
    <span class="dot"></span>
    <span class="name">CASA MARLO</span>
  </div>

  <address class="address">
    42 Lowden Road<br>Windsor<br>03 9555 0142
  </address>

  <svg class="contact" width="849" height="1200" viewBox="0 0 849 1200">
    <rect class="square" x="536" y="988" width="46" height="46"/>
    <text x="592" y="1024" font-size="30" textLength="244" lengthAdjust="spacingAndGlyphs">/CASAMARLORESTAURANTS</text>
    <text x="536" y="1076" font-size="30" textLength="300" lengthAdjust="spacingAndGlyphs">HTTP://WWW.CASAMARLO.EXAMPLE</text>
  </svg>
</main>
</body>
</html>
```